Parkinson's Disease Progression

Visually describe the rate of Parkinson progression in the first 15 years following diagnosis. Title: "Patient-Perceived Progression of Parkinsonism"

The attached figure names "meanqol" is the curve that should serve as the basis of this graphic. Everything else-- color, labels, font, etc. describe this curve.
Thank you!

Target Market(s)

People with Parkisnon's Disease, neurologists, family members.

Font styles to use
Sans Serif

Requirements
Must have
• Must have the lines going through these exact numbers
Excellent -- 502
Very good- 661
Good- 895
Fair- 1268
Poor- 1655

LABELS:
Title: "Patient-Perceived Progression of Parkinsonism"
"SAW-MX (Self-Assessed Wellbeing Index for Movement Conditions)" should be the label on the left.
"Quality of Life" should be the label on the right
"Years Since Diagnosis" should be the label on the bottom
Nice to have
• A color scheme that goes from GOOD (low numbers) to BAD (high numbers).

Easy to read (elderly)

```html
<!DOCTYPE html>
<html lang="en">
<head>
<meta charset="utf-8">
<title>Patient-Perceived Progression of Parkinsonism</title>
<link href="https://fonts.googleapis.com/css2?family=Inter:wght@600;700;800&display=swap" rel="stylesheet">
<style>
  :root {
    --ink: #111111;
    --paper: #ffffff;
    --poor: #ee4768;
    --fair: #f49a97;
    --good: #f9cfad;
    --very-good: #c5c8a9;
    --excellent: #86ae9a;
    --mean-line: #1aade8;
    --interval-edge: #34456a;
  }
  html, body {
    margin: 0;
    padding: 0;
    width: 1200px;
    height: 785px;
    overflow: hidden;
    background: var(--paper);
  }
  .progression-chart {
    display: block;
    width: 1200px;
    height: 785px;
    font-family: "Inter", Arial, sans-serif;
  }
  .band-poor { fill: var(--poor); }
  .band-fair { fill: var(--fair); }
  .band-good { fill: var(--good); }
  .band-very-good { fill: var(--very-good); }
  .band-excellent { fill: var(--excellent); }
  .band-label { fill: var(--paper); font-size: 22px; font-weight: 700; }
  .axis-line, .tick { stroke: var(--ink); stroke-width: 4; fill: none; }
  .tick-minor { stroke: var(--ink); stroke-width: 2.5; }
  .tick-label { fill: var(--ink); font-size: 31px; font-weight: 700; }
  .axis-title { fill: var(--ink); font-size: 46px; font-weight: 800; }
  .axis-subtitle { fill: var(--ink); font-size: 17px; font-weight: 700; }
  .confidence-band { fill: var(--paper); }
  .confidence-edge { fill: none; stroke: var(--interval-edge); stroke-width: 1.5; stroke-dasharray: 4 3; }
  .mean-curve { fill: none; stroke: var(--mean-line); stroke-width: 6; stroke-linecap: round; }
</style>
</head>
<body>
<svg class="progression-chart" viewBox="0 0 1380 902" xmlns="http://www.w3.org/2000/svg" role="img" aria-label="Mean wellbeing score rising over 15 years since diagnosis, moving from Excellent toward Fair quality of life">
  <!-- quality bands -->
  <g class="quality-bands">
    <rect class="band-poor" x="305" y="111" width="878" height="144"/>
    <rect class="band-fair" x="305" y="255" width="878" height="138"/>
    <rect class="band-good" x="305" y="393" width="878" height="87"/>
    <rect class="band-very-good" x="305" y="480" width="878" height="59"/>
    <rect class="band-excellent" x="305" y="539" width="878" height="187"/>
  </g>

  <!-- confidence interval -->
  <path class="confidence-band" d="M305,525 C360,510 420,480 490,465 C540,452 570,445 620,443 C680,440 730,445 770,430 C830,410 860,395 890,380 C930,360 960,345 1010,330 C1080,312 1140,300 1183,268 L1183,375 C1150,368 1120,362 1095,367 C1060,370 1040,370 1010,380 C960,395 930,405 890,420 C840,440 800,458 770,460 C720,465 670,466 620,470 C580,475 560,475 540,480 C480,500 430,530 420,540 C380,560 340,570 305,600 Z"/>
  <path class="confidence-edge" d="M305,525 C360,510 420,480 490,465 C540,452 570,445 620,443 C680,440 730,445 770,430 C830,410 860,395 890,380 C930,360 960,345 1010,330 C1080,312 1140,300 1183,268"/>
  <path class="confidence-edge" d="M305,600 C340,570 380,560 420,540 C430,530 480,500 540,480 C560,475 580,475 620,470 C670,466 720,465 770,460 C800,458 840,440 890,420 C930,405 960,395 1010,380 C1040,370 1060,370 1095,367 C1120,362 1150,368 1183,375"/>

  <!-- mean curve -->
  <path class="mean-curve" d="M305,564 C360,545 420,520 480,495 C520,478 550,465 600,458 C650,452 700,455 750,450 C800,443 840,420 890,399 C940,378 970,362 1010,352 C1060,340 1120,330 1183,321"/>

  <!-- band labels -->
  <g class="band-labels">
    <text class="band-label" x="890" y="185">Poor (1269-1655)</text>
    <text class="band-label" x="890" y="304">Fair (896-1268)</text>
    <text class="band-label" x="890" y="441">Good (661-895)</text>
    <text class="band-label" x="890" y="515">Very Good (503-660)</text>
    <text class="band-label" x="890" y="627">Excellent (0-502)</text>
  </g>

  <!-- axes -->
  <line class="axis-line" x1="305" y1="57" x2="305" y2="726"/>
  <line class="axis-line" x1="1183" y1="57" x2="1183" y2="726"/>
  <line class="axis-line" x1="285" y1="726" x2="1183" y2="726"/>

  <!-- y ticks -->
  <g class="y-ticks">
    <line class="tick" x1="285" y1="57" x2="325" y2="57"/>
    <line class="tick" x1="285" y1="131" x2="325" y2="131"/>
    <line class="tick" x1="285" y1="206" x2="325" y2="206"/>
    <line class="tick" x1="285" y1="280" x2="325" y2="280"/>
    <line class="tick" x1="285" y1="354" x2="325" y2="354"/>
    <line class="tick" x1="285" y1="429" x2="325" y2="429"/>
    <line class="tick" x1="285" y1="503" x2="325" y2="503"/>
    <line class="tick" x1="285" y1="577" x2="325" y2="577"/>
    <line class="tick" x1="285" y1="652" x2="325" y2="652"/>
    <line class="tick-minor" x1="295" y1="94" x2="315" y2="94"/>
    <line class="tick-minor" x1="295" y1="169" x2="315" y2="169"/>
    <line class="tick-minor" x1="295" y1="243" x2="315" y2="243"/>
    <line class="tick-minor" x1="295" y1="317" x2="315" y2="317"/>
    <line class="tick-minor" x1="295" y1="392" x2="315" y2="392"/>
    <line class="tick-minor" x1="295" y1="466" x2="315" y2="466"/>
    <line class="tick-minor" x1="295" y1="540" x2="315" y2="540"/>
    <line class="tick-minor" x1="295" y1="615" x2="315" y2="615"/>
    <line class="tick-minor" x1="295" y1="689" x2="315" y2="689"/>
  </g>
  <g class="y-labels" text-anchor="end">
    <text class="tick-label" x="272" y="68">1800</text>
    <text class="tick-label" x="272" y="142">1600</text>
    <text class="tick-label" x="272" y="217">1400</text>
    <text class="tick-label" x="272" y="291">1200</text>
    <text class="tick-label" x="272" y="365">1000</text>
    <text class="tick-label" x="272" y="440">800</text>
    <text class="tick-label" x="272" y="514">600</text>
    <text class="tick-label" x="272" y="588">400</text>
    <text class="tick-label" x="272" y="663">200</text>
  </g>

  <!-- x ticks -->
  <g class="x-ticks">
    <line class="tick" x1="305" y1="706" x2="305" y2="746"/>
    <line class="tick" x1="598" y1="706" x2="598" y2="746"/>
    <line class="tick" x1="890" y1="706" x2="890" y2="746"/>
    <line class="tick" x1="1183" y1="706" x2="1183" y2="746"/>
    <line class="tick-minor" x1="364" y1="714" x2="364" y2="736"/>
    <line class="tick-minor" x1="422" y1="714" x2="422" y2="736"/>
    <line class="tick-minor" x1="481" y1="714" x2="481" y2="736"/>
    <line class="tick-minor" x1="539" y1="714" x2="539" y2="736"/>
    <line class="tick-minor" x1="656" y1="714" x2="656" y2="736"/>
    <line class="tick-minor" x1="715" y1="714" x2="715" y2="736"/>
    <line class="tick-minor" x1="773" y1="714" x2="773" y2="736"/>
    <line class="tick-minor" x1="832" y1="714" x2="832" y2="736"/>
    <line class="tick-minor" x1="949" y1="714" x2="949" y2="736"/>
    <line class="tick-minor" x1="1007" y1="714" x2="1007" y2="736"/>
    <line class="tick-minor" x1="1066" y1="714" x2="1066" y2="736"/>
    <line class="tick-minor" x1="1124" y1="714" x2="1124" y2="736"/>
  </g>
  <g class="x-labels" text-anchor="middle">
    <text class="tick-label" x="260" y="784">0</text>
    <text class="tick-label" x="598" y="784">5</text>
    <text class="tick-label" x="890" y="784">10</text>
    <text class="tick-label" x="1183" y="784">15</text>
  </g>

  <!-- axis titles -->
  <text class="axis-title" text-anchor="middle" transform="translate(100 392) rotate(-90)">SAW-MX</text>
  <text class="axis-subtitle" text-anchor="middle" transform="translate(140 392) rotate(-90)">(Self-Assessed Wellbeing Index for Movement Conditions)</text>
  <text class="axis-title" text-anchor="middle" transform="translate(1290 370) rotate(-90)">Quality of Life</text>
  <text class="axis-title" text-anchor="middle" x="732" y="860">Years Since Diagnosis</text>
</svg>
</body>
</html>
```